Flyerdesign Faltblatt 6 seitiger Wickelfalz - Querformat -  DIN lang
Flyerdesign Faltblatt 6 seitiger Wickelfalz - Querformat - DIN lang
Zielgruppe
Das Geschäft samtweich kosmetik & wellness, bietet Kosmetik und Wellnessbehandlungen an. Zu Werbezwecken soll ein Faltblatt erstellt werden.
Siehe http://kosmetik-mirbental.de
Aufgabenstellung
Ein modernes FLYER-Design zu erstellen.
Faltblatt - 6-seitig Wickelfalz - DIN Lang - Querformat (Gesamtmaße: 63 cm x 10 cm)
Es gibt bereits ein fertiges Webdesign, auf dessen Basis ein passendes Design für einen Wickelfalz-Flyer erstellt werden soll.
Das Faltblatt sollte an meine Homepage angepasst sein. Eine Auswahl von Fotos und das Logo sind als Dateien beigefügt. Ebenfalls beigefügt ist ein Beispiel-Flyer in CS3 Indesign, dessen Abmessungen übernommen werden müssen. In diesem Beispielflyer sind alle Texte hinterlegt, die auch im neu zu erstellenden Flyerdesign verwendet werden müssen.
Die im Beispielflyer vorhandenen 6 Seiten sind in dieser Aufteilung bezogen auf die dort hinterlegten Texte zu übernehmen. Das Datenformat und der Beschnitt sind aus dem Beispiel-Flyer zu übernehmen.
Der neu zu erstellende Flyer ist als Adobe CS3 Indesign Datei zu liefern.

```html
<!DOCTYPE html>
<html lang="de">
<head>
<meta charset="utf-8">
<title>samtweich kosmetik &amp; wellness – Faltblatt Innenseite</title>
<link href="https://fonts.googleapis.com/css2?family=Fira+Sans:wght@400;600;700&display=swap" rel="stylesheet">
<style>
  :root {
    --paper: #ffffff;
    --panel: #c9c0b7;
    --accent: #d8412a;
    --brand: #8a2b2b;
    --ink: #3b3b3b;
    --swoosh: #ddd5cd;
    --photo-light: #f1e3da;
    --photo-dark: #b48a74;
  }
  * { box-sizing: border-box; margin: 0; padding: 0; }
  html, body { width: 1200px; height: 550px; overflow: hidden; background: var(--paper); }
  body { font-family: "Fira Sans", Arial, sans-serif; color: var(--ink); }

  .flyer { position: relative; width: 1200px; height: 550px; background: var(--paper); overflow: hidden; }

  .swoosh { position: absolute; left: 0; top: 0; width: 827px; height: 550px; }

  .headline {
    position: absolute; left: 45px; top: 172px;
    font-size: 40px; font-weight: 700; color: var(--accent); letter-spacing: 0.2px;
  }

  .offer { position: absolute; top: 236px; width: 357px; font-size: 16px; line-height: 21px; }
  .offer--facial { left: 45px; }
  .offer--voucher { left: 435px; }
  .offer__title { color: var(--accent); font-weight: 400; }
  .offer__text { text-align: justify; }

  .offer__meta {
    display: flex; justify-content: flex-end; align-items: center; gap: 8px;
    margin-top: 8px; color: var(--accent); font-size: 14px;
  }
  .offer__meta svg { width: 18px; height: 18px; display: block; }
  .offer__meta span { margin-right: 8px; }

  .photo {
    position: absolute; left: 629px; top: 54px; width: 162px; height: 167px;
    border-radius: 16px;
    background: radial-gradient(circle at 55% 55%, var(--photo-light) 0%, #e2c4b2 50%, var(--photo-dark) 100%);
  }

  .contact-panel {
    position: absolute; left: 827px; top: 0; width: 373px; height: 550px;
    background: var(--panel); padding: 84px 0 0 32px;
    font-size: 19px; line-height: 22px;
  }
  .brand-name { color: var(--brand); font-size: 23px; font-weight: 400; line-height: 28px; margin-bottom: 50px; }
  .contact-panel__name { font-weight: 600; }
  .contact-panel__block { margin-bottom: 20px; }
  .contact-panel__phone { display: flex; gap: 58px; }
  .contact-panel__hours { margin-top: 32px; }
</style>
</head>
<body>
<main class="flyer">
  <svg class="swoosh" viewBox="0 0 827 550" aria-hidden="true">
    <path d="M380 0 C 520 80, 660 170, 827 300" fill="none" stroke="var(--swoosh)" stroke-width="16" stroke-linecap="round"/>
  </svg>

  <div class="photo" role="img" aria-label="Foto: entspannte Kundin bei einer Gesichtsbehandlung"></div>

  <h1 class="headline">Exklusiv für Sie</h1>

  <section class="offer offer--facial">
    <h2 class="offer__title">Gesichtsbehandlung für Neukunden<br>Sind Sie Neukunde?</h2>
    <p class="offer__text">Dann empfehlen wir Ihnen unsere Gesichtsbehandlung zum Kennenlernen. Nach einer Augenbrauenkorrektur und einem sanften hautschonenden Peeling können Sie bei einer Gesichts-, Hals- und Decolleté-Massage entspannen.</p>
    <p>Mit Wirkstoffampulle, Tagespflege und Make-Up.</p>
    <div class="offer__meta">
      <svg viewBox="0 0 18 18" aria-hidden="true"><circle cx="9" cy="9" r="9" fill="var(--accent)"/><path d="M9 4v5h4" fill="none" stroke="#fff" stroke-width="1.8"/></svg>
      <span>30 Min</span>
      <svg viewBox="0 0 18 18" aria-hidden="true"><circle cx="9" cy="9" r="9" fill="var(--accent)"/><text x="9" y="13" text-anchor="middle" font-size="11" font-weight="700" fill="#fff" font-family="Fira Sans, sans-serif">€</text></svg>
      <span>40 Euro</span>
    </div>
  </section>

  <section class="offer offer--voucher">
    <h2 class="offer__title">Geschenkgutschein<br>Die ideale Geschenk-Idee für Sie oder Ihn</h2>
    <p class="offer__text">Verschenken Sie Zeit zum Wohlfühlen. Ein Gutschein für eine Gesichts- oder Wellness-Behandlung ist ein Geschenk der besonderen Art und für jeden Anlass geeignet. Gerne stellen wir Ihnen einen Gutschein – auch als Geschenk verpackt – aus.</p>
  </section>

  <aside class="contact-panel">
    <p class="brand-name">samtweich kosmetik &amp; wellness</p>
    <div class="contact-panel__block">
      <p class="contact-panel__name">Miriam Albers</p>
      <p>Kosmetikerin/Krankenschwester</p>
    </div>
    <div class="contact-panel__block">
      <p>Lindenweg 12</p>
      <p>48599 Mirbental</p>
    </div>
    <div class="contact-panel__block">
      <p class="contact-panel__phone"><span>Telefon</span><span>02599 557310</span></p>
      <p>samtweich@kos-mirbental.de</p>
      <p>kosmetik-mirbental.de</p>
    </div>
    <p class="contact-panel__hours">Termine nach telefonischer<br>Vereinbarung</p>
  </aside>
</main>
</body>
</html>
```